Home Delivery Startup needs a web design!

Hello,
We're a start-up company in the final mile logistics industry. Our name is Brightwater Freight Collective. We partner with retailers throughout the USA and Canada and can perform the following services:
Home Delivery
Warehousing
Assembly
We like grey tones and an ability to incorporate our logo and it's colors throughout the site.
We pride ourselves as being a customizable logistics solution .
Our=comprehensive customer support and advanced technology systems make us distinguishable for every delivery solution.
Strategically located distribution centers throughout North America give us an advantage to get product to customers quickly, safely and conveniently, with consistent, efficient service.
Target Market(s)
Retailers in the US and Canada
Industry/Entity Type
Industry
Coding
Coded - Design and coding required
Number of Pages Required
5+ page

```html
<!DOCTYPE html>
<html lang="en">
<head>
<meta charset="utf-8">
<title>Brightwater Freight Collective</title>
<link href="https://fonts.googleapis.com/css2?family=Roboto:wght@300;400;500;700&display=swap" rel="stylesheet">
<style>
:root{
  --orange:#f04e1a;
  --ink:#2b2b2b;
  --dark:#141619;
  --dark-2:#1e2227;
  --grey:#e2e2e2;
  --mute:#8a8f96;
  --white:#ffffff;
}
*{box-sizing:border-box;margin:0;padding:0}
html,body{width:682px;height:1200px;overflow:hidden;background:var(--white)}
body{font-family:'Roboto',Arial,sans-serif;color:var(--ink);position:relative}
a{color:inherit;text-decoration:none}

.topbar{height:21px;display:flex;justify-content:flex-end;align-items:center;gap:14px;padding-right:48px;font-size:7px;color:#777}
.topbar .account span{margin:0 5px}
.topbar .tollfree{display:flex;align-items:center;gap:4px}
.topbar .tollfree strong{font-size:11px;color:#333;font-weight:700;letter-spacing:.3px}

.masthead{height:52px;background:#0d0d0e;display:flex;align-items:center;justify-content:space-between;padding:0 48px}
.brand{color:var(--white);font-weight:700;font-size:16px;letter-spacing:.2px;text-transform:uppercase}
.mainnav{display:flex;gap:26px;font-size:7.5px;font-weight:500;color:var(--white)}
.mainnav .active{color:var(--orange)}

.hero{height:271px;background:linear-gradient(170deg,#3b4042 0%,#4a5050 35%,#2f3436 60%,#555a5a 100%)}

.welcome{height:114px;padding-top:24px;text-align:center}
.section-title{display:flex;align-items:center;justify-content:center;gap:10px;font-weight:300;font-size:20px;letter-spacing:.5px;color:#333}
.section-title::before,.section-title::after{content:"";width:165px;height:1px;background:#ccc}
.welcome p{width:570px;margin:12px auto 0;font-size:7px;line-height:13px;color:#666}

.services{height:263px;background:linear-gradient(180deg,var(--dark-2),var(--dark));padding-top:10px}
.services .section-title{color:var(--white)}
.services .section-title::before,.services .section-title::after{background:#555;width:195px}
.cards{display:flex;gap:20px;padding:0 49px;margin-top:16px}
.card{width:182px;text-align:center}
.card h3{height:24px;line-height:24px;background:#2f3338;color:var(--white);font-size:10px;font-weight:700}
.card .photo{height:124px}
.card p{font-size:6px;line-height:9px;color:#cfd2d6;margin:5px 4px 0}
.btn{display:inline-block;margin-top:8px;background:var(--orange);color:var(--white);font-size:6.5px;font-weight:700;padding:5px 13px}

.about{position:absolute;top:748px;left:0;width:682px;height:210px;display:flex;background:var(--grey)}
.about .collage{width:350px;height:210px;background:linear-gradient(135deg,#8a6b4c 0%,#b28a5e 30%,#e07a3c 45%,#9aa3ab 65%,#c2c8ce 100%)}
.about .copy{padding:14px 26px 0 22px;flex:1}
.about .section-title{font-size:18px;color:var(--orange);justify-content:flex-start}
.about .section-title::before{width:56px}.about .section-title::after{width:50px}
.about h4{font-size:7.5px;font-weight:700;margin-top:12px;color:#222}
.about p{font-size:7.5px;line-height:12.5px;color:#555;margin-top:6px}

.footer{position:absolute;top:972px;left:0;width:682px;height:228px;color:var(--white)}
.footer-bg{position:absolute;inset:0;background:linear-gradient(180deg,#202326 0%,#2a2e31 55%,#191b1d 100%)}
.footer h5{font-size:10px;font-weight:400;color:var(--orange);margin-bottom:14px}
.fcol{position:absolute;top:15px}
.fnav{left:49px}.ffollow{left:295px}.floc{left:535px}
.fnav ul{list-style:none;font-size:6px;line-height:11px;color:#ddd}
.fnav li:first-child{color:var(--orange)}
.social{display:flex;gap:7px}
.social span{width:18px;height:18px;border-radius:50%;background:#555}
.social span:first-child{background:var(--orange)}
.loc li{list-style:none;display:flex;gap:8px;font-size:5.5px;line-height:9px;color:#ddd;margin-bottom:7px}
.loc b{font-weight:700;color:var(--white)}
.loc svg{flex:none;margin-top:1px}
.fbottom{position:absolute;left:0;right:0;top:190px;height:38px;border-top:1px solid #3a3e42;display:flex;align-items:center;gap:18px;padding-left:49px}
.fbottom .brand{font-size:13px}
.fbottom small{font-size:6.5px;color:#ccc}
.totop{position:absolute;right:0;top:1163px;width:25px;height:21px;background:var(--orange);display:flex;align-items:center;justify-content:center}
</style>
</head>
<body>
<div class="topbar">
  <div class="account"><a>Create an account</a><span>|</span><a>Login</a></div>
  <div class="tollfree">
    <svg width="8" height="9" viewBox="0 0 10 10"><path d="M2 0l2 2.5-1 1.2c.6 1.3 1.7 2.4 3 3l1.2-1L10 8 8.5 10C4 9.5.5 6 0 1.5z" fill="#f04e1a"/></svg>
    <span>Call Us Toll Free:</span><strong>284 5550-1937</strong>
  </div>
</div>

<header class="masthead">
  <a class="brand">Brightwater Freight</a>
  <nav class="mainnav"><a class="active">HOME</a><a>ABOUT</a><a>SERVICES</a><a>BLOG</a><a>CONTACT US</a></nav>
</header>

<div class="hero" role="img" aria-label="Truck driving along a highway beneath a rocky hillside, dark grey tint"></div>

<section class="welcome">
  <h2 class="section-title">WELCOME TO OUR SITE!</h2>
  <p>Lorem ipsum dolor sit amet, consectetur adipiscing elit. Etiam eget bibendum tortor. Aliquam ac neque in turpis pharetra pharetra. Sed nec blandit diam. Integer molestie aliquam luctus. Pellentesque imperdiet hendrerit felis sit amet finibus. Nulla tristique sem vitae fringilla posuere. Morbi at purus a arcu dignissim fringilla vel at lectus. Nulla non orci a leo feugiat molestie. Mauris in magna lacinia, ornare est eget, placerat purus.</p>
</section>

<section class="services">
  <h2 class="section-title">OUR SERVICES</h2>
  <div class="cards">
    <article class="card">
      <h3>Home Delivery</h3>
      <div class="photo" role="img" aria-label="Illustration of movers loading boxes into a truck" style="background:linear-gradient(135deg,#f4f4f4,#d9c2a0 55%,#9fb8d8)"></div>
      <p>Lorem ipsum dolor sit amet conse ctetur adipi sicing elit, sed do eiusmod tempor incididunt ut labore et dolore magna aliqua.</p>
      <a class="btn">READ MORE</a>
    </article>
    <article class="card">
      <h3>Warehousing</h3>
      <div class="photo" role="img" aria-label="Forklift moving stacked cartons in a warehouse" style="background:linear-gradient(135deg,#c9a37a,#a47e58 50%,#d8662e 75%,#6d5a48)"></div>
      <p>Lorem ipsum dolor sit amet conse ctetur adipi sicing elit, sed do eiusmod tempor incididunt ut labore et dolore magna aliqua.</p>
      <a class="btn">READ MORE</a>
    </article>
    <article class="card">
      <h3>Assembly</h3>
      <div class="photo" role="img" aria-label="Assembly workshop with workbenches" style="background:linear-gradient(180deg,#c5c8c4,#8f8a6a 50%,#e8e8e6)"></div>
      <p>Lorem ipsum dolor sit amet conse ctetur adipi sicing elit, sed do eiusmod tempor incididunt ut labore et dolore magna aliqua.</p>
      <a class="btn">READ MORE</a>
    </article>
  </div>
</section>

<section class="about">
  <div class="collage" role="img" aria-label="Collage of shelving, a scissor lift, tanker trucks, containers and a cargo plane"></div>
  <div class="copy">
    <h2 class="section-title">ABOUT US</h2>
    <h4>LOREM IPSUM DOLOR SIT AMET CONSE CTETUR ADIPI SICING ELIT</h4>
    <p>Lorem ipsum dolor sit amet conse ctetur adipi sicing elit, sed do eius-mod tempor incididunt ut labore et dolore magna aliqua. Ut enim ad minim veniam, quis nostrud exercitation ullamco laboris nisi ut aliquip ex.Lorem ipsum dolor sit amet conse ctetur adipi sicing elit, sed do eiusmod tempor incididunt ut labore et dolore magna aliqua. Ut enim ad minim veniam, quis nostrud exercitation ullamco laboris nisi ut aliquip ex.</p>
  </div>
</section>

<footer class="footer">
  <div class="footer-bg" role="img" aria-label="Container ship at sea under a dark overlay"></div>
  <div class="fcol fnav">
    <h5>Navigation</h5>
    <ul><li>HOME</li><li>ABOUT</li><li>SERVICES</li><li>BLOG</li><li>CONTACT US</li></ul>
  </div>
  <div class="fcol ffollow">
    <h5>FOLLOW US</h5>
    <div class="social"><span></span><span></span><span></span></div>
  </div>
  <div class="fcol floc">
    <h5>OUR LOCATION</h5>
    <ul class="loc">
      <li><svg width="8" height="8" viewBox="0 0 10 10"><path d="M5 1L0 5h1.5v4h2.5V6.5h2V9h2.5V5H10z" fill="#f04e1a"/></svg><span>48 Harbour Row,<br>Lakeport, LP 04 K7 2R.</span></li>
      <li><svg width="8" height="8" viewBox="0 0 10 10"><path d="M2 0l2 2.5-1 1.2c.6 1.3 1.7 2.4 3 3l1.2-1L10 8 8.5 10C4 9.5.5 6 0 1.5z" fill="#f04e1a"/></svg><span>Telephone: <b>+284 5550-1937</b></span></li>
      <li><svg width="8" height="8" viewBox="0 0 10 10"><rect x="1" y="3" width="8" height="6" fill="#f04e1a"/><rect x="3" y="0" width="4" height="3" fill="#f04e1a"/></svg><span>FAX: <b>+1 844 555 0174</b></span></li>
    </ul>
  </div>
  <div class="fbottom">
    <span class="brand">Brightwater Freight</span>
    <small>© 2015 | Privacy Policy</small>
  </div>
</footer>
<a class="totop" aria-label="Back to top"><svg width="10" height="7" viewBox="0 0 10 7"><path d="M1 6l4-4 4 4" stroke="#fff" stroke-width="1.6" fill="none"/></svg></a>
</body>
</html>
```